New Web Page Design - Cement Rendering Business

Looking for a overhaul of our existing website (www.olpa.com.au).

Looking for a sleek and elegant design that incorporates the colours of our logos, black / green and white. Needs to look professional and want it to be well above what our competition is offering. (Zorbix search for 'cement rendering sydney' will display the competition we want to be well ahead of.

Prefer a mixture of pages with black background and white alternatively between home (black), about us (white), contact us (black) and gallery (white).

Would like to incorporate our logo on all pages attached preferably in the top left corner.

Website needs to be search engine optimised and have easily updated photo gallery which we already have.

Also need to embed our zorbix metrics code on the front home page.

Website needs to be able easily updated (text, pictures ) as required.
content management system should include fields where you can alter your page titles, meta description and keywords.

Pages also needs to be optimised for mobile devices, kelphone, kelpad and other mobile devices. (it is a current feature we have)

If you have any questions, just message me.

Please remember the look and feel of the site is important to us, we don't want it over complicated, simple elegant and professional in line with our logo standards.
Updates

Hi All, As an example of the look and feel we like. We have found a site that may assist in your design and creative process. http://beta.marvodesk.org/ We like the simplicity, elegance and professional look of this site, although we would like it with our images, colours and logos. I hope this helps.! keep the great designs coming!

All, Thanks for the designs. Please try and use our website images due to copyright reasons for all your designs. Boris

Target Market(s)

Construction Companies

Industry/Entity Type

Business

Colors
9bcb3b
acd036
474747

Requirements
Must have
• Search Engine Optimised.
Photo Gallery
Elegant/Professional Look & Feel.
Simple Yet Effective
Nice to have
• Moving Parts
Should not have
• Overly Complicated.
Cheap & Traditional Looking.
Boring

```html
<!DOCTYPE html>
<html lang="en">
<head>
<meta charset="utf-8">
<title>OLPA Cement Rendering</title>
<link href="https://fonts.googleapis.com/css2?family=Open+Sans:ital,wght@0,300;0,400;0,600;0,700;1,400&family=Oswald:wght@500&family=Roboto+Condensed:ital,wght@1,700&display=swap" rel="stylesheet">
<style>
:root{
  --green:#8dbb3a;
  --green-dark:#6f9a2a;
  --green-soft:#9bcb3b;
  --ink:#2a2a2a;
  --ink-deep:#1e1e1e;
  --panel:#333333;
  --text:#474747;
  --muted:#777777;
  --line:#dddddd;
  --white:#ffffff;
}
*{box-sizing:border-box;margin:0;padding:0}
html,body{width:746px;height:1200px;overflow:hidden}
body{position:relative;font-family:"Open Sans",Arial,sans-serif;color:var(--text);background:var(--white)}
.abs{position:absolute}

/* header */
.site-header{left:0;top:0;width:746px;height:87px;background:var(--ink)}
.brand{left:180px;top:18px}
.brand-name{font-size:34px;font-weight:300;color:var(--green);letter-spacing:1px;line-height:44px}
.contact-box{top:12px;height:32px;border:1px solid #555;border-radius:3px;background:var(--ink-deep);color:var(--white);padding:3px 6px;display:flex;align-items:center;justify-content:space-between}
.contact-box small{display:block;font-size:7px;font-weight:600}
.contact-box b{display:block;font-size:10.5px;font-weight:600}
.call-box{left:421px;width:103px}
.mail-box{left:533px;width:125px}
.main-nav{left:334px;top:53px;height:24px;display:flex;background:#3a3a3a}
.main-nav a{display:block;height:24px;line-height:24px;font-size:9.5px;color:#eee;text-decoration:none;text-align:center;border-right:1px solid #2a2a2a}
.main-nav a.active{background:var(--green);color:var(--white)}

/* hero */
.hero{left:0;top:87px;width:746px;height:303px;background:radial-gradient(ellipse at 68% 48%,#8fae5a 0%,#7d9266 30%,#6b7a5c 70%,#5d6a52 100%)}
.hero-title{left:360px;top:190px;width:280px;text-align:center;font-family:"Oswald",sans-serif;font-size:23px;line-height:30px;color:#f5f5f0;font-weight:500;transform:scaleX(.88)}
.hero-title em{display:block;font-family:"Roboto Condensed",sans-serif;font-style:italic;font-weight:700;color:#3b4a2a;font-size:23px}
.hero-dots{left:611px;top:371px;display:flex;gap:5px}
.hero-dots i{width:7px;height:7px;border-radius:50%;background:var(--white)}
.hero-dots i:first-child{background:#444}

/* welcome */
.welcome-title{left:82px;top:408px;display:flex;align-items:center;gap:10px;font-size:17px;font-weight:600;color:var(--ink);height:30px}
.welcome-title .brand-name{font-size:19px;line-height:30px;color:var(--ink)}
.welcome-rule{left:82px;top:449px;width:360px;height:1px;background:linear-gradient(90deg,transparent,#ccc,transparent)}
.welcome-text{left:82px;top:462px;width:366px;font-size:9.2px;line-height:14.8px;color:var(--muted)}
.btn{display:block;background:var(--green);color:var(--white);font-weight:700;text-align:center;border-radius:3px;text-decoration:none}
.read-more{left:82px;top:562px;width:54px;height:20px;line-height:20px;font-size:8.5px}

.services{left:484px;top:406px;width:180px;height:184px;background:#f4f4f4;border-top:3px solid var(--green);box-shadow:0 3px 4px rgba(0,0,0,.2)}
.services-head{height:29px;background:var(--ink-deep);display:flex;align-items:center;gap:5px;padding-left:4px;color:var(--white);font-size:15px;font-weight:400}
.services-head .ico{width:25px;height:25px;border-radius:50%;background:var(--white)}
.services ul{list-style:none;padding:2px 8px 0}
.services li{height:17.8px;line-height:17.5px;font-size:9px;color:#333;border-bottom:1px dotted #ccc;display:flex;align-items:center;gap:8px;padding-left:2px}
.services li:last-child{border-bottom:none}

/* feature band */
.feature-band{left:0;top:602px;width:746px;height:238px;background:var(--panel)}
.card{top:628px;width:180px;height:186px;background:#f7f7f7;border-radius:4px}
.card-head{position:absolute;left:-3px;top:8px;width:186px;height:25px;background:var(--green);display:flex;align-items:center;gap:8px;padding-left:9px;color:var(--white);font-size:11px;font-weight:700;box-shadow:0 2px 2px rgba(0,0,0,.15)}
.card-head .ico{width:25px;height:25px;border-radius:50%;background:var(--white);border:2px solid var(--ink-deep);display:flex;align-items:center;justify-content:center}
.card-link{position:absolute;right:14px;bottom:10px;font-size:6.5px;font-weight:700;color:var(--green-dark)}
.quote{position:absolute;left:13px;top:46px;width:160px;height:98px;background:#e9e9e9;border-radius:4px;padding:6px 5px;font-size:6.9px;line-height:11px;font-style:italic;color:#444;letter-spacing:-.1px}
.quote-mark{font-size:13px;color:#aaa;font-weight:700;line-height:0}
.quote-name{position:absolute;left:74px;top:128px;font-size:7.6px;color:var(--green-dark)}
.avatar{position:absolute;left:23px;top:128px;width:48px;height:48px;border-radius:50%;background:linear-gradient(#6a7f9a,#2d3848);border:3px solid var(--white)}
.why-list{position:absolute;left:8px;top:47px;width:164px;list-style:none}
.why-list li{height:30px;display:flex;gap:8px;font-size:7.2px;line-height:9.8px;color:#444;border-bottom:1px solid var(--line);padding-top:4px}
.why-list li:last-child{border-bottom:none}
.field{position:absolute;left:8px;width:166px;height:17px;border:1px solid #ccc;background:var(--white);font-size:7px;color:#666;padding:3px 5px;border-radius:2px}
.submit{position:absolute;left:8px;top:165px;width:42px;height:13px;line-height:13px;font-size:8px}

/* gallery */
.gallery-tab{left:276px;top:840px;width:188px;height:24px;background:var(--ink-deep);color:var(--white);text-align:center;line-height:24px;font-size:13px;font-weight:600;clip-path:polygon(0 0,100% 0,92% 100%,8% 100%)}
.thumb{top:880px;width:139px;height:122px;border:1px solid #ccc;border-radius:3px;background:var(--white);text-align:center}
.thumb-photo{height:92px;border-radius:2px 2px 0 0}
.thumb b{display:block;margin-top:4px;font-size:8px;color:var(--green-dark)}
.thumb i{display:block;font-size:7px;color:#444}
.arrow{top:928px;width:24px;height:24px;border-radius:50%;background:#e6e6e6;display:flex;align-items:center;justify-content:center}

/* footer */
.footer-bg{left:0;top:1016px}
.foot-title{font-size:12px;color:var(--white);font-weight:400;padding-bottom:4px;border-bottom:1px dotted #888;width:100px}
.quick-links{left:85px;top:1062px}
.quick-links ul{list-style:none;margin-top:4px}
.quick-links li{height:15.2px;font-size:7.4px;color:var(--white)}
.quick-links li::before{content:"› ";color:#aaa}
.newsletter{left:204px;top:1062px;width:125px}
.newsletter .foot-title{width:125px}
.newsletter p{font-size:7.2px;color:var(--white);line-height:10px;margin-top:5px}
.email-input{left:204px;top:1115px;width:125px;height:15px;background:var(--white);border-radius:2px;font-size:7px;font-style:italic;color:#555;padding:2px 6px 0 18px}
.subscribe{left:204px;top:1140px;width:50px;height:14px;line-height:14px;font-size:8px}
.map{left:375px;top:1104px;width:174px;height:59px;background:linear-gradient(135deg,#e8e4d6,#d9d3c0);border:2px solid var(--white)}
.foot-brand{left:588px;top:1068px;width:60px;text-align:center;font-size:14px;font-weight:300;color:var(--green)}
.social{left:590px;top:1144px;display:flex;gap:4px}
.social i{width:16px;height:16px;border-radius:50%;background:var(--white)}
.copyright{left:0;top:1176px;width:746px;height:24px;background:var(--ink-deep);color:#ddd;font-size:7.5px;text-align:center;line-height:24px}
</style>
</head>
<body>

<header class="site-header abs">
  <div class="brand abs"><span class="brand-name">OLPA</span></div>
  <div class="contact-box call-box abs"><div><small>Call Now:</small><b>(02) 9471 3386</b></div>
    <svg width="14" height="16" viewBox="0 0 14 16"><path d="M3 1h3l1 4-2 1c1 2 2 4 4 5l1-2 4 1v3c-6 1-12-6-11-12z" fill="#8dbb3a"/></svg></div>
  <div class="contact-box mail-box abs"><div><small>Email us:</small><b>works@olpa.com.au</b></div>
    <svg width="16" height="12" viewBox="0 0 16 12"><rect x="0.5" y="0.5" width="15" height="11" fill="#8dbb3a"/><path d="M1 1l7 6 7-6" stroke="#1e1e1e" fill="none"/></svg></div>
  <nav class="main-nav abs">
    <a class="active" style="width:58px">HOME</a>
    <a style="width:83px">ABOUT US</a>
    <a style="width:111px">PHOTO GALLERY</a>
    <a style="width:72px">CONTACT</a>
  </nav>
</header>

<section class="hero abs" role="img" aria-label="Photo of a trowel spreading fresh cement render with a green splash texture"></section>
<h1 class="hero-title abs">OLPA is your one stop<br>shop for all your<em>cement rendering needs</em></h1>
<div class="hero-dots abs"><i></i><i></i><i></i><i></i></div>

<h2 class="welcome-title abs">WELCOME TO <span class="brand-name">OLPA</span></h2>
<div class="welcome-rule abs"></div>
<p class="welcome-text abs">Lorem ipsum dolor sit amet, consectetuer adipiscing elit, sed diam nonummy nibh euismod tincidunt ut laoreet dolore magna aliquam erat volutpat. Ut wisi enim ad minim veniam, quis nostrud exerci tation ullamcorper suscipit lobortis nisl ut aliquip ex ea commodo consequat. Duis autem vel eum iriure dolor in hendrerit in vulputate velit esse molestie consequat, vel illum dolore eu feugiat nulla facilisis at vero eros et accumsan et iusto odio dignissim qui blandit.</p>
<a class="btn read-more abs">Read More</a>

<aside class="services abs">
  <div class="services-head"><span class="ico"><svg width="25" height="25" viewBox="0 0 25 25"><path d="M7 7l11 11M18 7L7 18" stroke="#1e1e1e" stroke-width="2.4" stroke-linecap="round"/></svg></span>Our Services</div>
  <ul>
    <li><svg width="8" height="7"><path d="M1 4l2 2 4-5" stroke="#6f9a2a" stroke-width="1.5" fill="none"/></svg>Cement Rendering</li>
    <li><svg width="8" height="7"><path d="M1 4l2 2 4-5" stroke="#6f9a2a" stroke-width="1.5" fill="none"/></svg>Mac-Render</li>
    <li><svg width="8" height="7"><path d="M1 4l2 2 4-5" stroke="#6f9a2a" stroke-width="1.5" fill="none"/></svg>Acrylic Render</li>
    <li><svg width="8" height="7"><path d="M1 4l2 2 4-5" stroke="#6f9a2a" stroke-width="1.5" fill="none"/></svg>White Setting</li>
    <li><svg width="8" height="7"><path d="M1 4l2 2 4-5" stroke="#6f9a2a" stroke-width="1.5" fill="none"/></svg>Blue Board Rendering</li>
    <li><svg width="8" height="7"><path d="M1 4l2 2 4-5" stroke="#6f9a2a" stroke-width="1.5" fill="none"/></svg>Concrete Repairs</li>
    <li><svg width="8" height="7"><path d="M1 4l2 2 4-5" stroke="#6f9a2a" stroke-width="1.5" fill="none"/></svg>All Types of Patch Up Works</li>
    <li><svg width="8" height="7"><path d="M1 4l2 2 4-5" stroke="#6f9a2a" stroke-width="1.5" fill="none"/></svg>Repairs</li>
  </ul>
</aside>

<section class="feature-band abs"></section>

<div class="card abs" style="left:83px">
  <div class="card-head"><span class="ico"><svg width="14" height="12" viewBox="0 0 14 12"><path d="M1 1h8v5H4l-2 2V6H1z M10 4h3v5h-1v2l-2-2H6V7h4z" fill="#1e1e1e"/></svg></span>CLIENT TESTIMONIALS</div>
  <div class="quote"><span class="quote-mark">“</span> Lorem ipsum dolor sit amet conseceuer adipiscing sed diam nonummy nibh euismod tincidunt ut laoreet dolore magna quam erat volutpat. Ut wisi enim ad minim veniam, quis nostrud exerci tation ullamcorper suscipitjj lobortis nisl ut ullamcorper suscipi.</div>
  <div class="avatar" role="img" aria-label="Client portrait"></div>
  <div class="quote-name">Mr. Dolore Magna</div>
  <div class="card-link">Read All Testimonials »</div>
</div>

<div class="card abs" style="left:282px">
  <div class="card-head"><span class="ico"><b style="font-size:12px;color:#1e1e1e">?</b></span>WHY CHOOSE US</div>
  <ul class="why-list">
    <li><svg width="10" height="9"><path d="M1 5l3 3 5-7" stroke="#6f9a2a" stroke-width="2" fill="none"/></svg><span>Lorem ipsum dolor sit amet, This consec teteur adipiscing elit</span></li>
    <li><svg width="10" height="9"><path d="M1 5l3 3 5-7" stroke="#6f9a2a" stroke-width="2" fill="none"/></svg><span>Lorem ipsum dolor sit amet, This consec teteur adipiscing elit</span></li>
    <li><svg width="10" height="9"><path d="M1 5l3 3 5-7" stroke="#6f9a2a" stroke-width="2" fill="none"/></svg><span>Lorem ipsum dolor sit amet, This consec teteur adipiscing elit</span></li>
    <li><svg width="10" height="9"><path d="M1 5l3 3 5-7" stroke="#6f9a2a" stroke-width="2" fill="none"/></svg><span>Lorem ipsum dolor sit amet, This consec teteur adipiscing elit</span></li>
  </ul>
  <div class="card-link">Read All FAQ's »</div>
</div>

<div class="card abs" style="left:480px">
  <div class="card-head"><span class="ico"><svg width="14" height="10" viewBox="0 0 14 10"><rect x="0.5" y="0.5" width="13" height="9" fill="none" stroke="#1e1e1e"/><path d="M1 1l6 5 6-5" stroke="#1e1e1e" fill="none"/></svg></span>QUICK CONTACT</div>
  <div class="field" style="top:46px">Name</div>
  <div class="field" style="top:74px">Email</div>
  <div class="field" style="top:98px">Phone</div>
  <div class="field" style="top:121px;height:38px">Message</div>
  <a class="btn submit">Submit</a>
</div>

<div class="gallery-tab abs">PHOTO GALLERY</div>
<div class="arrow abs" style="left:48px"><svg width="8" height="10"><path d="M6 1L2 5l4 4" stroke="#999" stroke-width="1.5" fill="none"/></svg></div>
<div class="arrow abs" style="left:669px"><svg width="8" height="10"><path d="M2 1l4 4-4 4" stroke="#999" stroke-width="1.5" fill="none"/></svg></div>
<div class="thumb abs" style="left:81px"><div class="thumb-photo" role="img" aria-label="Worker in hi-vis shirt rendering a wall" style="background:linear-gradient(135deg,#8a8470,#b9b08f 50%,#5e6a3a)"></div><b>Lorem ipsum dolor</b><i>seddiam no nummy nibh</i></div>
<div class="thumb abs" style="left:229px"><div class="thumb-photo" role="img" aria-label="Hand spreading render with a trowel" style="background:linear-gradient(135deg,#c9c6be,#e0d9cc 50%,#d88a6a)"></div><b>Lorem ipsum dolor</b><i>seddiam no nummy nibh</i></div>
<div class="thumb abs" style="left:377px"><div class="thumb-photo" role="img" aria-label="Rendered house exterior" style="background:linear-gradient(180deg,#3d6fa8 0%,#6d6456 40%,#a08060 100%)"></div><b>Lorem ipsum dolor</b><i>seddiam no nummy nibh</i></div>
<div class="thumb abs" style="left:524px"><div class="thumb-photo" role="img" aria-label="Gloved hand smoothing a rendered wall" style="background:linear-gradient(135deg,#bdbdbd,#dadada 60%,#e08a3a)"></div><b>Lorem ipsum dolor</b><i>seddiam no nummy nibh</i></div>

<svg class="footer-bg abs" width="746" height="160" viewBox="0 0 746 160">
  <path d="M0 12 C180 -4 360 10 520 30 C560 35 575 40 582 45 C590 80 645 80 654 45 C680 32 720 28 746 26 V160 H0Z" fill="#8dbb3a"/>
  <path d="M0 20 C180 4 360 18 520 38 C560 43 572 48 578 53 C588 92 648 92 657 53 C682 40 720 36 746 34 V160 H0Z" fill="#2e2e2e"/>
</svg>
<div class="foot-brand abs">OLPA</div>

<div class="quick-links abs">
  <div class="foot-title">Quick Links</div>
  <ul><li>Home</li><li>About Us</li><li>Photo Gallery</li><li>Our Project</li><li>Contact Us</li></ul>
</div>
<div class="newsletter abs">
  <div class="foot-title">Newsletter</div>
  <p>Subscribe to our newsletter to<br>our special offers , discounts</p>
</div>
<div class="email-input abs">your e-mail address</div>
<a class="btn subscribe abs">Subscribe</a>
<div class="map abs" role="img" aria-label="Street map showing the business location"></div>
<div class="social abs"><i></i><i></i><i></i></div>

<footer class="copyright abs">© 2014 OLPA Cement Rendering. All Rights Reserved</footer>
</body>
</html>
```